Bolera Brisa

Website for a night club with live music and cabaret dancers. I would like to have the following Menu: 1.) Home; 2) The Facilities; 3) The Show; 4) Other Attractions; 5) Videos & Fotos; 6) Program; 7) Reservations; 8) Membership; 9) Contacts.

The pages should be easily editable and allow to enter text, including the menu since the final version will be in both English and Portuguese. It should have a toggle or links for the Portuguese language and the English Language.

The night club itself is called "BOLERA BRISA"; and its URL is www.bolerabrisa-example.com.

Industry/Entity Type

Night Club

```html
<!DOCTYPE html>
<html lang="en">
<head>
<meta charset="utf-8">
<title>Bolera Brisa — Night Club</title>
<link href="https://fonts.googleapis.com/css2?family=Michroma&family=Open+Sans:wght@400;600;700&display=swap" rel="stylesheet">
<style>
:root{
  --black:#000;
  --nav:#262626;
  --nav-line:#3a3a3a;
  --red:#b31d18;
  --red-dark:#8f1410;
  --white:#fff;
  --text:#d6d6d6;
  --muted:#a8a8a8;
  --heading:#cfcfcf;
  --footer:#232323;
  --footer-bottom:#111;
  --gold:#f2a93b;
}
*{margin:0;padding:0;box-sizing:border-box}
html,body{width:900px;height:1200px;overflow:hidden;background:var(--black)}
body{position:relative;font-family:"Open Sans",Arial,sans-serif;color:var(--text)}
.abs{position:absolute}

/* navigation */
.main-nav{position:absolute;top:0;left:0;width:900px;height:36px;background:linear-gradient(#2f2f2f,#1d1d1d);z-index:5}
.main-nav ul{list-style:none;display:flex;position:absolute;left:77px;top:0;height:36px}
.main-nav li{height:36px;line-height:35px;padding:0 10.5px;font-size:11.4px;font-weight:600;color:#e8e8e8;border-right:1px solid var(--nav-line);white-space:nowrap}
.main-nav li:last-child{border-right:none}
.main-nav li.active{background:var(--red);position:relative;padding:0 10px}
.main-nav li.active::after{content:"";position:absolute;left:50%;bottom:-7px;margin-left:-7px;border:7px solid transparent;border-bottom:none;border-top-color:var(--red)}

/* hero */
.stage-backdrop{left:0;top:36px;width:900px;height:540px;background:
  radial-gradient(ellipse 380px 120px at 450px 20px,#ffd37a 0%,#f0a033 40%,transparent 100%),
  linear-gradient(180deg,#f6b640 0%,#e38f22 18%,#8a3f0c 42%,#1a0700 68%,#000 100%)}
.brand{left:77px;top:68px;font-family:"Michroma",sans-serif;font-size:23px;color:#111;letter-spacing:.5px}
.lang{left:646px;top:83px;display:flex;align-items:center;gap:6px;font-size:8px;font-weight:700;color:#222}
.lang .flag{width:13px;height:9px;background:linear-gradient(#b22 0 50%,#eee 50% 100%);position:relative}
.lang .flag::before{content:"";position:absolute;left:0;top:0;width:6px;height:5px;background:#2a3f8a}
.lang .caret{width:0;height:0;border:3px solid transparent;border-top-color:#666;margin-top:3px}
.book-btn{left:717px;top:76px;width:108px;height:26px;background:var(--red);border:1px solid var(--red-dark);border-radius:2px;color:#fff;font-size:12px;text-align:center;line-height:24px}

.slider{left:75px;top:134px;width:751px;height:397px;background:#111;border:4px solid #111}
.slide-photo{position:absolute;inset:0;background:
  radial-gradient(ellipse 90px 70px at 140px 80px,#e8d23a,transparent),
  radial-gradient(ellipse 90px 70px at 300px 80px,#e8d23a,transparent),
  radial-gradient(ellipse 90px 70px at 460px 80px,#e8d23a,transparent),
  radial-gradient(ellipse 90px 70px at 620px 80px,#e8d23a,transparent),
  linear-gradient(180deg,#4a4a45 0%,#5a6a3a 40%,#6a7a4a 70%,#3c3a35 100%)}
.slide-arrow{position:absolute;top:183px;width:26px;height:26px;border-radius:50%;background:rgba(255,255,255,.55)}
.slide-arrow svg{display:block}
.slide-arrow.prev{left:18px}
.slide-arrow.next{right:18px;background:rgba(255,255,255,.35)}
.slide-caption{position:absolute;left:119px;top:340px;width:497px;height:40px;background:var(--red);color:#fff;font-size:17.5px;line-height:40px;text-align:center}

/* content columns */
.section-title{font-family:"Michroma",sans-serif;font-size:19px;color:var(--heading);top:575px}
.divider{top:653px;width:1px;height:133px;background:#333}
.more-link{top:842px;font-size:11px;color:var(--text);text-decoration:underline}

.polaroid{background:#fff;box-shadow:0 2px 6px rgba(0,0,0,.6)}
.polaroid .pic{position:absolute;left:9px;top:9px;right:9px;bottom:40px}
.polaroid .cap{position:absolute;left:0;right:0;bottom:10px;text-align:center;font-size:12px;color:#444}

.welcome-lead{left:371px;top:617px;width:200px;font-size:11.5px;line-height:16.5px;color:#eee}
.welcome-thumb{left:374px;top:676px;width:70px;height:65px;background:linear-gradient(#9aa8b2 0 30%,#3d4a3a 30% 100%)}
.welcome-side{left:463px;top:670px;width:110px;font-size:9.6px;line-height:13.6px;color:var(--text)}
.welcome-body{left:374px;top:748px;width:200px;font-size:9.6px;line-height:13.6px;color:var(--text)}

.events-lead{left:628px;top:617px;font-size:14px;color:#eee}
.event{left:629px;width:200px;height:60px}
.event .thumb{position:absolute;left:0;top:2px;width:59px;height:54px}
.event h4{position:absolute;left:73px;top:0;font-size:11.6px;font-weight:400;color:#fff}
.event .date{position:absolute;left:73px;top:17px;font-size:8px;color:var(--muted)}
.event p{position:absolute;left:73px;top:31px;width:130px;font-size:9.6px;line-height:13px;color:var(--text)}

/* footer */
.site-footer{left:0;top:926px;width:900px;height:223px;background:var(--footer)}
.footer-col{top:49px;width:180px}
.footer-col h5{font-size:10.4px;font-weight:600;letter-spacing:1px;color:#fff;margin-bottom:10px}
.footer-col p{font-size:8px;line-height:13.6px;color:var(--muted)}
.footer-brand{font-family:"Michroma",sans-serif;font-size:15.5px;color:#fff;margin:2px 0 8px}
.more-about{font-size:8px;font-weight:700;color:#bbb;display:flex;justify-content:space-between;width:165px;margin-top:8px}
.socials{display:flex;gap:12px;margin-top:12px}
.socials span{width:11px;height:11px;border-radius:50%;background:#fff}
.news-grid{display:grid;grid-template-columns:80px 80px;gap:3px 4px}
.news-grid div{height:52px}
.contact-list{margin-top:10px;font-size:8px;color:var(--muted);list-style:none}
.contact-list li{display:flex;align-items:center;gap:7px;height:13.6px}
.subscribe{display:flex;margin-top:9px;width:172px;height:24px;background:#333;border:1px solid #3c3c3c;border-radius:2px;align-items:center;padding:0 2px 0 7px;justify-content:space-between}
.subscribe span{font-size:8px;color:#888}
.subscribe b{background:var(--red);color:#fff;font-size:7.2px;letter-spacing:.4px;padding:5px 6px;border-radius:1px}
.bottom-bar{left:0;top:1149px;width:900px;height:51px;background:var(--footer-bottom);text-align:center;line-height:50px;font-size:9.6px;color:var(--muted)}
</style>
</head>
<body>

<nav class="main-nav">
  <ul>
    <li class="active">Home</li><li>The Facilities</li><li>The Show</li><li>Other Attractions</li><li>Videos &amp; Fotos</li><li>Program</li><li>Reservations</li><li>Membership</li><li>Contacts</li>
  </ul>
</nav>

<div class="abs stage-backdrop" role="img" aria-label="Concert stage with bright lights and a cheering crowd"></div>

<div class="abs brand">Bolera Brisa</div>
<div class="abs lang"><span class="flag"></span>ENG<span class="caret"></span></div>
<div class="abs book-btn">Book Now</div>

<section class="abs slider">
  <div class="slide-photo" role="img" aria-label="Four cabaret dancers in colourful feathered headdresses and costumes"></div>
  <div class="slide-arrow prev"><svg width="26" height="26" viewBox="0 0 26 26"><path d="M15 7l-6 6 6 6" fill="none" stroke="#333" stroke-width="2.2"/></svg></div>
  <div class="slide-arrow next"><svg width="26" height="26" viewBox="0 0 26 26"><path d="M11 7l6 6-6 6" fill="none" stroke="#fff" stroke-width="2"/></svg></div>
  <div class="slide-caption">We are night club with live music and cabaret dancers</div>
</section>

<!-- gallery -->
<h2 class="abs section-title" style="left:75px">Gallery</h2>
<div class="abs polaroid" style="left:128px;top:640px;width:160px;height:170px;transform:rotate(12deg)">
  <div class="pic" role="img" aria-label="Club light show" style="background:linear-gradient(135deg,#3a2a6a,#b03a8a,#2a2a4a)"></div>
  <div class="cap">Lorem ipsum</div>
</div>
<div class="abs polaroid" style="left:110px;top:630px;width:160px;height:175px;transform:rotate(-14deg)">
  <div class="pic" role="img" aria-label="Crowd on the dance floor under purple lights" style="background:linear-gradient(160deg,#d8c8f0,#8a5ab8,#2a1a3a)"></div>
  <div class="cap">ipsum</div>
</div>
<div class="abs polaroid" style="left:84px;top:652px;width:160px;height:170px;transform:rotate(-28deg)">
  <div class="pic" role="img" aria-label="Cabaret dancer in costume on promotional poster" style="background:linear-gradient(150deg,#6a1a1a,#c8402a,#e0a030,#2a4a2a)"></div>
  <div class="cap">Lorem ipsum</div>
</div>
<a class="abs more-link" style="left:250px">View All</a>

<div class="abs divider" style="left:340px"></div>

<!-- welcome -->
<h2 class="abs section-title" style="left:367px">Welcome</h2>
<p class="abs welcome-lead">Sed lorem nibh, pharetra congue diam ut, lacinia gravida lacus.</p>
<div class="abs welcome-thumb" role="img" aria-label="Club building exterior with palm trees"></div>
<p class="abs welcome-side">Morbi ultrices feugiat odio ac porttitor. Nunc eget est sed odio fermentum hendrerit quis ut magna.</p>
<p class="abs welcome-body">Sed lorem nibh, pharetra congue diam ut, lacinia gravida lacus. Morbi ultrices feugiat odio ac porttitor. Nunc eget est</p>
<a class="abs more-link" style="left:505px">Read More</a>

<div class="abs divider" style="left:596px"></div>

<!-- events -->
<h2 class="abs section-title" style="left:624px">Latest Events</h2>
<p class="abs events-lead">Sed lorem nibh</p>
<div class="abs event" style="top:649px">
  <div class="thumb" role="img" aria-label="Blue laser light show" style="background:radial-gradient(circle at 50% 50%,#7ad0f0,#1a4a8a 50%,#05101a)"></div>
  <h4>Lorem ipsum</h4><div class="date">14-03-2014 &nbsp;- &nbsp;8 pm</div>
  <p>Morbi ultrices feugiat odio ac porttitor.</p>
</div>
<div class="abs event" style="top:725px">
  <div class="thumb" role="img" aria-label="DJ mixing desk under red lights" style="background:linear-gradient(160deg,#e0306a,#3a1a4a 55%,#0a1a3a)"></div>
  <h4>Lorem ipsum</h4><div class="date">14-03-2014 &nbsp;- &nbsp;8 pm</div>
  <p>Morbi ultrices feugiat odio ac porttitor.</p>
</div>
<a class="abs more-link" style="left:777px">View All</a>

<!-- footer -->
<footer class="abs site-footer">
  <div class="abs footer-col" style="left:78px">
    <h5>WHO WE ARE</h5>
    <div class="footer-brand">Bolera Brisa</div>
    <p>Magnis modipsae voloratati andigen daepe-ditem quiate re porem que aut labor. Laceaque eictemperum quiae sitiorem rest non restibusaes maio es dem tumquam.</p>
    <div class="more-about"><span>More about us</span><span>&#8594;</span></div>
    <div class="socials"><span></span><span></span><span></span><span></span></div>
  </div>
  <div class="abs footer-col" style="left:270px">
    <h5>LATEST NEWS</h5>
    <div class="news-grid">
      <div role="img" aria-label="Friends taking a photo at the club" style="background:linear-gradient(135deg,#c89a7a,#3a5a9a)"></div>
      <div role="img" aria-label="Dark dance floor with red lights" style="background:linear-gradient(135deg,#3a0a0a,#a02a2a,#1a0a0a)"></div>
      <div role="img" aria-label="Lit dance floor in blue" style="background:linear-gradient(180deg,#2a2aa0,#5a7ae0,#1a1a6a)"></div>
      <div role="img" aria-label="Group of friends posing" style="background:linear-gradient(135deg,#6a9ab8,#c04a6a,#3a3a3a)"></div>
    </div>
  </div>
  <div class="abs footer-col" style="left:461px;width:170px">
    <h5>GET IN TOUCH</h5>
    <p>Doloreiur quia commolu ptatemp dolupta orepererum tibusam eumenis et consent accullignis dentibea autem inisita.</p>
    <ul class="contact-list">
      <li><svg width="6" height="8" viewBox="0 0 6 8"><path d="M3 0a3 3 0 0 0-3 3c0 2 3 5 3 5s3-3 3-5a3 3 0 0 0-3-3z" fill="#aaa"/></svg>84 Street, City, State 24813</li>
      <li><svg width="6" height="8" viewBox="0 0 6 8"><rect x="1" y="0" width="4" height="8" rx="1" fill="none" stroke="#aaa"/></svg>+00 (123) 456 78 90</li>
      <li><svg width="7" height="6" viewBox="0 0 7 6"><rect x=".5" y=".5" width="6" height="5" fill="none" stroke="#aaa"/><path d="M.5 .5l3 3 3-3" fill="none" stroke="#aaa"/></svg>info@bolerabrisa-example.com</li>
    </ul>
  </div>
  <div class="abs footer-col" style="left:653px">
    <h5>FREE UPDATES</h5>
    <p>Conecus iure posae volor remped modis aut lor volor accabora incim resto explabo.</p>
    <div class="subscribe"><span>Enter your email address</span><b>SUBSCRIBE</b></div>
  </div>
</footer>
<div class="abs bottom-bar">© 2014 bolerabrisa-example.com. All rights reserved.</div>

</body>
</html>
```